Trade show Booth Design

We implement continuous improvement programs - we use "lean" and "six sigma" to improve efficiency in both manufacturing and service delivery environments. We are looking to build a graphic for our marketing trade show booth. We have the booth picked out from a size perspective - 8' wide and has a dye sublimated fabric - we need the graphic. It needs to draw people in, so it can be simple but direct - i have attached our logo which should be prominent

```html
<!DOCTYPE html>
<html lang="en">
<head>
<meta charset="utf-8">
<title>Briskline Trade Show Booth Graphic</title>
<link href="https://fonts.googleapis.com/css2?family=Archivo+Black&family=Bebas+Neue&family=Questrial&display=swap" rel="stylesheet">
<style>
  :root {
    --blue-deep: #0a3a72;
    --blue-mid: #0d5aa6;
    --silver-light: #f2f3f5;
    --silver-mid: #c9ccd1;
    --silver-dark: #9ea3aa;
    --icon-silver: #e3e5e8;
    --navy-text: #0b2d5c;
    --white: #ffffff;
  }
  * { margin: 0; padding: 0; box-sizing: border-box; }
  html, body { width: 1200px; height: 797px; overflow: hidden; }
  body { background: #e9e9ea; }
  .booth-graphic {
    position: relative;
    width: 1200px;
    height: 797px;
    background: radial-gradient(ellipse at 50% 55%, var(--blue-mid) 0%, #0a4a8f 45%, var(--blue-deep) 100%);
    overflow: hidden;
  }
  .brand {
    position: absolute;
    top: 170px;
    left: 0;
    width: 100%;
    display: flex;
    justify-content: center;
    align-items: center;
    gap: 22px;
  }
  .brand-dot {
    width: 54px; height: 54px;
    border-radius: 50%;
    background: var(--silver-mid);
  }
  .brand-name {
    font-family: "Questrial", sans-serif;
    font-size: 78px;
    letter-spacing: 8px;
    color: var(--silver-mid);
    line-height: 1;
  }
  .tagline {
    position: absolute;
    top: 278px;
    width: 100%;
    text-align: center;
    font-family: "Bebas Neue", sans-serif;
    font-size: 26px;
    letter-spacing: 4px;
    color: var(--silver-mid);
  }
  .message-band {
    position: absolute;
    top: 334px;
    left: 0;
    width: 100%;
    height: 111px;
    background: linear-gradient(90deg, var(--silver-dark) 0%, var(--silver-light) 30%, #ffffff 50%, var(--silver-light) 70%, var(--silver-dark) 100%);
    text-align: center;
    color: var(--navy-text);
  }
  .message-lead {
    font-family: "Archivo Black", sans-serif;
    font-size: 29px;
    letter-spacing: 1.5px;
    margin-top: 12px;
    line-height: 1.1;
  }
  .message-main {
    font-family: "Bebas Neue", sans-serif;
    font-size: 56px;
    font-weight: 400;
    letter-spacing: 0.5px;
    line-height: 1;
    margin-top: 4px;
  }
  .pillars {
    position: absolute;
    top: 500px;
    left: 0;
    width: 100%;
    height: 240px;
  }
  .pillar {
    position: absolute;
    width: 260px;
    text-align: center;
    transform: translateX(-50%);
  }
  .pillar svg { display: block; margin: 0 auto; }
  .pillar-label {
    font-family: "Questrial", sans-serif;
    font-size: 22px;
    line-height: 1.2;
    color: var(--white);
    margin-top: 22px;
  }
  .pillar--process { left: 263px; }
  .pillar--excellence { left: 620px; }
  .pillar--growth { left: 964px; }
  .pillar--growth .pillar-label { margin-top: 14px; }
</style>
</head>
<body>
<main class="booth-graphic">
  <div class="brand">
    <span class="brand-dot"></span>
    <span class="brand-name">BRISKLINE</span>
  </div>
  <p class="tagline">Streamline. Refine. Deliver</p>

  <section class="message-band">
    <p class="message-lead">IMPROVE EFFICIENCY IN BOTH</p>
    <h1 class="message-main">MANUFACTURING AND SERVICE DELIVERY ENVIRONMENTS</h1>
  </section>

  <section class="pillars">
    <div class="pillar pillar--process">
      <svg width="180" height="150" viewBox="0 0 180 150" aria-hidden="true">
        <defs>
          <linearGradient id="cycle-silver" x1="0" y1="0" x2="1" y2="1">
            <stop offset="0" stop-color="#ffffff"/>
            <stop offset="0.5" stop-color="#c9ccd1"/>
            <stop offset="1" stop-color="#eef0f2"/>
          </linearGradient>
        </defs>
        <ellipse cx="90" cy="75" rx="74" ry="60" fill="none" stroke="url(#cycle-silver)" stroke-width="24" stroke-dasharray="90 14"/>
        <rect x="56" y="82" width="12" height="20" fill="var(--icon-silver)"/>
        <rect x="74" y="72" width="12" height="30" fill="var(--icon-silver)"/>
        <rect x="92" y="62" width="12" height="40" fill="var(--icon-silver)"/>
        <rect x="110" y="52" width="12" height="50" fill="var(--icon-silver)"/>
        <polyline points="54,70 76,54 92,62 118,40" fill="none" stroke="var(--icon-silver)" stroke-width="5"/>
        <polygon points="112,34 126,34 124,48" fill="var(--icon-silver)"/>
      </svg>
      <p class="pillar-label">PROCESS<br>IMPROVEMENT</p>
    </div>

    <div class="pillar pillar--excellence">
      <svg width="200" height="150" viewBox="0 0 200 150" aria-hidden="true">
        <rect x="12" y="6" width="150" height="126" rx="12" fill="none" stroke="var(--icon-silver)" stroke-width="9"/>
        <line x1="12" y1="34" x2="162" y2="34" stroke="var(--icon-silver)" stroke-width="6"/>
        <rect x="34" y="17" width="104" height="8" fill="var(--icon-silver)"/>
        <rect x="34" y="78" width="10" height="36" fill="var(--icon-silver)"/>
        <rect x="52" y="58" width="10" height="56" fill="var(--icon-silver)"/>
        <g transform="translate(150,96)">
          <circle r="34" fill="var(--icon-silver)"/>
          <g fill="var(--icon-silver)">
            <rect x="-9" y="-48" width="18" height="20"/>
            <rect x="-9" y="28" width="18" height="20"/>
            <rect x="-48" y="-9" width="20" height="18"/>
            <rect x="28" y="-9" width="20" height="18"/>
            <rect x="-9" y="-48" width="18" height="20" transform="rotate(45)"/>
            <rect x="-9" y="-48" width="18" height="20" transform="rotate(135)"/>
            <rect x="-9" y="-48" width="18" height="20" transform="rotate(225)"/>
            <rect x="-9" y="-48" width="18" height="20" transform="rotate(315)"/>
          </g>
          <circle r="14" fill="#0c4f95"/>
        </g>
      </svg>
      <p class="pillar-label">OPERATIONAL<br>EXCELLENCE</p>
    </div>

    <div class="pillar pillar--growth">
      <svg width="190" height="145" viewBox="0 0 190 145" aria-hidden="true">
        <rect x="20" y="100" width="14" height="34" fill="var(--icon-silver)"/>
        <rect x="42" y="86" width="14" height="48" fill="var(--icon-silver)"/>
        <rect x="64" y="92" width="14" height="42" fill="var(--icon-silver)"/>
        <rect x="86" y="72" width="14" height="62" fill="var(--icon-silver)"/>
        <rect x="108" y="66" width="14" height="68" fill="var(--icon-silver)"/>
        <rect x="130" y="50" width="14" height="84" fill="var(--icon-silver)"/>
        <polyline points="6,104 40,72 66,84 150,20" fill="none" stroke="var(--icon-silver)" stroke-width="9" stroke-linejoin="round"/>
        <polygon points="136,8 176,2 168,40" fill="var(--icon-silver)"/>
      </svg>
      <p class="pillar-label">GROWTH</p>
    </div>
  </section>
</main>
</body>
</html>
```